Bluewater Products Flyer

Bluewater Lending Group, Inc.
Licensed Mortgage Company
Serving the DMV since 1997
"You choose Bluewater, we'll carry it home"
We specialize in...
FHA Loans
* Credit Scores as low as 500
* 203K Renovation Loans
Conventional Loans
* As little as 1% Down
* Bank Statement for Self-Employed
Investor Loans
* DSCR, & Fix & Flip
* Commercial & New Construction
Other Programs
* HELOCS & Reverse Mortgages
Call today for a free consultation
(800) 641-2957
www.bluewaterlendhub.com
NMLS #731846

```html
<!DOCTYPE html>
<html lang="en">
<head>
<meta charset="utf-8">
<title>Bluewater Products Flyer</title>
<link rel="stylesheet" href="https://fonts.googleapis.com/css2?family=Kanit:ital,wght@1,700;1,800&family=Open+Sans:wght@400;600;700&display=swap">
<style>
  :root {
    --page: #e9e9e9;
    --paper: #f1f2f4;
    --navy: #0f2461;
    --blue: #1f73c4;
    --sky: #dbeaf7;
    --gold: #a8922e;
    --gold-light: #c9b453;
    --yellow: #f7d21c;
    --white: #ffffff;
    --ink: #1d2540;
  }
  * { margin: 0; padding: 0; box-sizing: border-box; }
  html, body { width: 1200px; height: 1137px; overflow: hidden; }
  body { background: var(--page); font-family: "Open Sans", Arial, sans-serif; position: relative; }

  .flyer {
    position: absolute; left: 141px; top: 110px; width: 906px; height: 907px;
    background: linear-gradient(180deg, #f4f5f7 0%, var(--paper) 60%, #e8ebef 100%);
    box-shadow: 0 2px 10px rgba(0,0,0,.18);
    overflow: hidden;
  }
  .headline-font { font-family: "Kanit", "Arial Black", sans-serif; font-style: italic; font-weight: 800; }

  .photo { position: absolute; left: 0; top: 0; }

  .banner-gold {
    position: absolute; left: 22px; top: 54px; width: 620px; height: 100px;
    background: linear-gradient(180deg, var(--gold-light) 0%, var(--gold) 55%, #8e7a22 100%);
    clip-path: polygon(4% 0, 100% 0, 96% 100%, 0 100%);
    border: 4px solid #d8d8d8;
  }
  .banner-gold span {
    position: absolute; left: 48px; top: 14px; font-size: 48px; color: var(--white);
    text-shadow: 2px 3px 2px rgba(0,0,0,.35); letter-spacing: .5px; white-space: nowrap;
  }
  .banner-light {
    position: absolute; left: 320px; top: 156px; width: 568px; height: 82px;
    background: linear-gradient(90deg, #ffffff 0%, #ffffff 45%, var(--sky) 100%);
    clip-path: polygon(4% 0, 100% 0, 96% 100%, 0 100%);
  }
  .banner-light span { position: absolute; left: 72px; top: 11px; font-size: 40px; color: var(--navy); white-space: nowrap; }
  .banner-light em { font-style: inherit; color: var(--blue); border-bottom: 4px solid var(--gold); }

  .brand {
    position: absolute; left: 668px; top: 36px; width: 220px; height: 100px;
    display: flex; align-items: center; justify-content: center; gap: 10px;
  }
  .brand-dot { width: 22px; height: 22px; border-radius: 50%; background: var(--blue); }
  .brand-name { font-family: "Kanit", sans-serif; font-style: italic; font-weight: 800; font-size: 34px; color: var(--navy); }

  .specialize { position: absolute; left: 569px; top: 268px; font-size: 32px; color: var(--navy); }
  .specialize em { font-style: inherit; color: var(--blue); }

  .program {
    position: absolute; left: 490px; width: 416px; background: var(--navy); color: var(--white);
    padding-left: 128px;
  }
  .program h3 { font-family: "Kanit", sans-serif; font-style: italic; font-weight: 700; font-size: 22px; color: var(--yellow); line-height: 1.1; }
  .program p { font-size: 16px; line-height: 21px; padding-left: 6px; }
  .program .tick { position: absolute; left: 96px; width: 20px; height: 20px; }

  .company { position: absolute; left: 628px; top: 744px; color: var(--ink); }
  .company strong { display: block; font-size: 17px; font-weight: 700; }
  .company span { display: block; font-size: 15px; line-height: 19px; }

  .contact {
    position: absolute; left: 530px; top: 812px; width: 376px; height: 95px;
    background: var(--blue); clip-path: polygon(7% 0, 100% 0, 100% 100%, 0 100%);
  }
  .contact-inner {
    position: absolute; left: 560px; top: 820px; width: 346px; height: 87px;
    background: var(--navy); clip-path: polygon(7% 0, 100% 0, 100% 100%, 0 100%);
    color: var(--white); padding: 4px 0 0 40px;
  }
  .contact-row { display: flex; align-items: center; gap: 10px; font-family: "Kanit", sans-serif; font-style: italic; font-weight: 700; font-size: 20px; line-height: 26px; }
  .contact-row svg { width: 18px; height: 18px; flex: none; }
  .nmls { font-family: "Kanit", sans-serif; font-style: italic; font-weight: 700; font-size: 14px; padding-left: 28px; }

  .cta-accent {
    position: absolute; left: 34px; top: 856px; width: 32px; height: 51px;
    background: var(--gold); clip-path: polygon(60% 0, 100% 0, 40% 100%, 0 100%);
  }
  .cta {
    position: absolute; left: 52px; top: 856px; width: 484px; height: 51px;
    background: var(--blue); clip-path: polygon(5% 0, 100% 0, 96% 100%, 0 100%);
    color: var(--white); font-size: 25px; padding: 5px 0 0 40px; white-space: nowrap;
  }
  .cta em { font-style: inherit; color: var(--yellow); }
</style>
</head>
<body>
<main class="flyer">
  <section class="program" style="top:312px;height:105px;padding-top:14px">
    <svg class="tick" style="top:17px" viewBox="0 0 20 20"><circle cx="10" cy="10" r="8.5" fill="none" stroke="#fff" stroke-width="1.6"/><path d="M6 10.5l3 3 6-7" fill="none" stroke="#fff" stroke-width="2"/></svg>
    <h3>Conventional Loans</h3>
    <p>* As little as 1% Down</p>
    <p>* Bank Statement for Self-Employed</p>
  </section>

  <section class="program" style="top:426px;height:104px;padding-top:14px">
    <svg class="tick" style="top:17px" viewBox="0 0 20 20"><circle cx="10" cy="10" r="8.5" fill="none" stroke="#fff" stroke-width="1.6"/><path d="M6 10.5l3 3 6-7" fill="none" stroke="#fff" stroke-width="2"/></svg>
    <h3>FHA Loans</h3>
    <p>* Credit Scores as low as 500</p>
    <p>* 203K Renovation Loans</p>
  </section>

  <section class="program" style="top:539px;height:105px;padding-top:14px">
    <svg class="tick" style="top:17px" viewBox="0 0 20 20"><circle cx="10" cy="10" r="8.5" fill="none" stroke="#fff" stroke-width="1.6"/><path d="M6 10.5l3 3 6-7" fill="none" stroke="#fff" stroke-width="2"/></svg>
    <h3>Investor Loans</h3>
    <p>* DSCR, &amp; Fix &amp; Flip</p>
    <p>* Commercial &amp; New Construction</p>
  </section>

  <section class="program" style="top:653px;height:74px;padding-top:12px">
    <svg class="tick" style="top:15px" viewBox="0 0 20 20"><circle cx="10" cy="10" r="8.5" fill="none" stroke="#fff" stroke-width="1.6"/><path d="M6 10.5l3 3 6-7" fill="none" stroke="#fff" stroke-width="2"/></svg>
    <h3>Other Programs</h3>
    <p>* HELOCS &amp; Reverse Mortgages</p>
  </section>

  <svg class="photo" width="906" height="907" viewBox="0 0 906 907">
    <defs>
      <linearGradient id="goldRing" x1="0" y1="0" x2="1" y2="1">
        <stop offset="0" stop-color="#c9b453"/>
        <stop offset="1" stop-color="#8e7a22"/>
      </linearGradient>
      <linearGradient id="photoTone" x1="0" y1="0" x2="0" y2="1">
        <stop offset="0" stop-color="#9c9a92"/>
        <stop offset=".45" stop-color="#d8d2c2"/>
        <stop offset=".7" stop-color="#6f8f4a"/>
        <stop offset="1" stop-color="#4e7a2c"/>
      </linearGradient>
    </defs>
    <circle cx="253" cy="505" r="323" fill="url(#goldRing)"/>
    <circle cx="216" cy="505" r="317" fill="#ffffff"/>
    <circle cx="212" cy="505" r="306" fill="url(#photoTone)" role="img" aria-label="Photo of a smiling family cheering in front of their new house, a child holding a home for sale sign"/>
  </svg>

  <div class="banner-gold"><span class="headline-font">You choose Bluewater</span></div>

  <div class="brand" aria-label="Bluewater">
    <span class="brand-dot"></span>
    <span class="brand-name">Bluewater</span>
  </div>

  <div class="banner-light"><span class="headline-font">We'll carry <em>it home</em></span></div>

  <div class="specialize headline-font">We speci<em>alize in:</em></div>

  <div class="company">
    <strong>Bluewater Lending Group, Inc.</strong>
    <span>Licensed Mortgage Company</span>
    <span>Serving the DMV since 1997</span>
  </div>

  <div class="contact"></div>
  <div class="contact-inner">
    <div class="contact-row">
      <svg viewBox="0 0 18 18"><circle cx="9" cy="9" r="9" fill="#f7d21c"/><path d="M6 4.5l2 2-1 1.3c.6 1.3 1.5 2.2 2.8 2.8l1.3-1 2 2-1.2 1.6c-3.4-.4-6.4-3.4-6.8-6.8z" fill="#0f2461"/></svg>
      <span>(800) 641-2957</span>
    </div>
    <div class="contact-row">
      <svg viewBox="0 0 18 18"><circle cx="9" cy="9" r="9" fill="#f7d21c"/><circle cx="9" cy="9" r="5" fill="none" stroke="#0f2461" stroke-width="1.3"/><path d="M4 9h10M9 4c-2.5 3-2.5 7 0 10M9 4c2.5 3 2.5 7 0 10" fill="none" stroke="#0f2461" stroke-width="1.1"/></svg>
      <span>www.bluewaterlendhub.com</span>
    </div>
    <div class="nmls">NMLS #731846</div>
  </div>

  <div class="cta-accent"></div>
  <div class="cta headline-font">Call today for a <em>FREE</em> consultation</div>
</main>
</body>
</html>
```